Webdesign für Dienstleistung im Industriebereich
Zielgruppe
Dienstleistung im Industriebereich.
Siehe Word Dokument
Aufgabenstellung
Design der Tochterfirma www.kefa.tools berücksichtigen

```html
<!DOCTYPE html>
<html lang="de">
<head>
<meta charset="utf-8">
<title>kefa systems – Services</title>
<link href="https://fonts.googleapis.com/css2?family=Arimo:wght@400;700&display=swap" rel="stylesheet">
<style>
:root{
  --red:#e01b2f;
  --ink:#2b2b2b;
  --nav:#6a6a6a;
  --muted:#777;
  --white:#fff;
  --header-top:#f1f1f1;
  --header-bottom:#d9d9d9;
}
*{box-sizing:border-box;margin:0;padding:0}
html,body{width:1200px;height:750px;overflow:hidden}
body{font-family:"Arimo",Helvetica,Arial,sans-serif;background:linear-gradient(#e4e4e4,#d2d2d2);position:relative;color:var(--ink)}
.site-header{position:absolute;left:0;top:0;width:1200px;height:119px;background:linear-gradient(180deg,var(--header-top),var(--header-bottom));border-bottom:1px solid #c4c4c4}
.brand{position:absolute;left:165px;top:32px;display:flex;align-items:center;gap:12px}
.brand-mark{width:54px;height:54px;background:var(--red)}
.brand-name{font-size:30px;font-weight:700;color:var(--red);letter-spacing:-0.5px}
.main-nav{position:absolute;left:450px;top:0;display:flex;height:79px;align-items:flex-end}
.main-nav a{font-size:23px;color:var(--nav);text-decoration:none;padding:0 18px 14px;line-height:1}
.main-nav a:first-child{padding-left:0}
.main-nav a.active{background:var(--red);color:var(--white);font-weight:700;height:79px;display:flex;align-items:flex-end;padding:0 5px 14px;margin:0 10px}
.hero{position:absolute;left:0;top:119px;width:1200px;height:476px;background:linear-gradient(100deg,#3a2412 0%,#8a5226 20%,#c07a3c 33%,#6e6058 48%,#a9aaac 62%,#d8d9db 75%,#8e8f92 90%,#bfc0c2 100%)}
.hero-title{position:absolute;left:0;right:0;top:96px;text-align:center;font-size:40px;font-weight:700;color:var(--white);letter-spacing:0.2px}
.hero-dots{position:absolute;left:568px;top:209px;display:flex;gap:4px}
.hero-dots span{width:13px;height:13px;border-radius:50%;background:#e8e8e8}
.service{position:absolute;top:428px;width:242px;height:322px;background:var(--white)}
.service h2{font-size:25px;font-weight:700;text-align:center;color:var(--ink);margin-top:12px;line-height:1.15}
.service h2.left{text-align:left;padding-left:20px;margin-top:9px}
.service p{font-size:13.6px;line-height:17px;color:#333;padding:0 10px 0 12px;margin-top:10px}
.service .more{color:var(--muted);margin-top:17px}
.service .photo{position:absolute;left:0;bottom:0;width:242px;height:131px}
</style>
</head>
<body>
<header class="site-header">
  <div class="brand"><div class="brand-mark"></div><span class="brand-name">kefa systems</span></div>
  <nav class="main-nav">
    <a href="#">Home</a><a href="#">about</a><a href="#">products</a><a class="active" href="#">services</a><a href="#">contact</a>
  </nav>
</header>

<section class="hero" role="img" aria-label="Geschwungene Metallfassade in Kupfer- und Silbertönen">
  <h1 class="hero-title">SERVICE AUF HÖCHSTEM NIVEAU.</h1>
  <div class="hero-dots"><span></span><span></span><span></span><span></span></div>
</section>

<article class="service" style="left:66px">
  <h2>MONTAGE</h2>
  <p>Kleben, schneiden, Sägen, Fügen, Clipsen oder kommissionieren. Wir verhelfen Ihnen zu Ihrem Ziel mit unserem spitzen Service.</p>
  <p class="more">...zusätzlicher Text</p>
  <div class="photo" role="img" aria-label="Trennschleifer beim Schneiden von Metall" style="background:linear-gradient(135deg,#c9c6c0,#5a5652 55%,#8d8780)"></div>
</article>

<article class="service" style="left:342px">
  <h2>LOGISTIK</h2>
  <p>Disposition der Bauteile, Frei Haus Lieferung der Ware oder eine gesamte Supplychain mit Finanzierung der Kaufteile. Wir bringen Sie an Ihr Ziel!</p>
  <p class="more">... zusätzlicher Text</p>
  <div class="photo" role="img" aria-label="Containerschiff auf See bei Abendlicht" style="background:linear-gradient(90deg,#5d4a44,#8a6d60 45%,#e0b89a 75%,#efd3bd)"></div>
</article>

<article class="service" style="left:616px">
  <h2 class="left">WARENAUSGABE<br>AUTOMATEN</h2>
  <p>Finanzierung, Leasing, Installation, Beffülung oder Betreuung wir unterstützen Sie!</p>
  <p class="more">... zusätzlicher Text</p>
  <div class="photo" role="img" aria-label="Lagerregale mit Kartons in einer Halle" style="background:linear-gradient(180deg,#8c7e6c,#b89f6e 50%,#c9b88f)"></div>
</article>

<article class="service" style="left:892px">
  <h2>BERATUNG</h2>
  <p>Einkaufsberatung mit Einstiegs-potentialanalyse, Industrie 4.0. mit Kanban, JIT und JIS Konzepte, Konsignationslagerkonzepte, Logistikberatung und Fracht-kostenreduktion.</p>
  <p class="more">...zusätzlicher Text</p>
  <div class="photo" role="img" aria-label="Berater am Schreibtisch mit Laptop vor orangem Hintergrund" style="background:linear-gradient(90deg,#e5731c,#f08a2c 45%,#cdd3dc 70%,#a9b3c2)"></div>
</article>
</body>
</html>
```